Etiketten-Design für Trinkweine
Zielgruppe
Wir sind eine Weinkellerei, die einfache Trinkweine für den LEH herstellt.
Unsere Zielgruppen sind Jugendliche .
Wir suchen ein Etikett für unser neues Produkt ,,Traubensaftschorle`` alkoholfrei
Aufgabenstellung
Siehe Anhang , eigene ideen sind auch erwünscht.
Das Etikett sollte Natur verbunden wirken da es ein Bio Produkt ist.
Farben: weiß, grün wären erwünscht.
Das Etikett sollte 75mm hoch und 120mm Breit sein
Strukturpapier weiß
Anbei auch unserer Standartetikett gerne kann das Logo übernommen werden

```html
<!DOCTYPE html>
<html lang="de">
<head>
<meta charset="utf-8">
<title>Traubensaft Etiketten</title>
<link href="https://fonts.googleapis.com/css2?family=Playfair+Display:wght@700;900&family=Open+Sans:wght@400;600&display=swap" rel="stylesheet">
<style>
  :root {
    --canvas: #f4f4f2;
    --yellow: #f3ea6b;
    --olive: #8fa444;
    --olive-soft: #a9b94f;
    --mint: #cfe5c3;
    --mint-deco: #dcecd3;
    --green: #2f9a3f;
    --green-dark: #1d6637;
    --ink: #111111;
  }
  * { box-sizing: border-box; margin: 0; padding: 0; }
  html, body { width: 1200px; height: 792px; overflow: hidden; background: var(--canvas); }
  .canvas { position: relative; width: 1200px; height: 792px; }

  .label {
    position: absolute; left: 320px; width: 560px; height: 350px; overflow: hidden;
    box-shadow: 0 6px 14px rgba(0,0,0,.18);
    font-family: "Open Sans", sans-serif;
  }
  .label--yellow { top: 26px; background: var(--yellow); }
  .label--green { top: 416px; background: var(--mint); }

  .art { position: absolute; }
  .art--leaf { left: 0; top: 0; width: 110px; height: 120px; border-radius: 40% 55% 50% 45%; }
  .art--grapes { left: 110px; top: 190px; width: 290px; height: 170px; border-radius: 50% 50% 10% 10%; }
  .art--vine { left: 300px; top: 100px; width: 110px; height: 150px; border-radius: 45% 55% 40% 50%; }
  .label--yellow .art--leaf, .label--yellow .art--vine { background: var(--olive); opacity: .85; }
  .label--yellow .art--grapes { background: radial-gradient(circle at 50% 40%, var(--olive-soft), var(--olive)); }
  .label--green .art { background: var(--mint-deco); }

  .divider-v { position: absolute; top: 0; bottom: 0; width: 3px; background: var(--ink); }
  .divider-v--left { left: 171px; }
  .divider-v--right { left: 384px; }
  .divider-h { position: absolute; left: 0; right: 0; height: 2px; background: var(--green); }
  .divider-h--top { top: 116px; }
  .divider-h--bottom { top: 246px; }

  .brand {
    position: absolute; left: 0; right: 0; text-align: center;
    font-family: "Playfair Display", serif; font-weight: 900; font-size: 30px; line-height: 1;
  }
  .label--yellow .brand { top: 38px; left: 174px; right: 176px; color: var(--ink); font-size: 26px; line-height: 1.05; }
  .label--green .brand { top: 36px; color: var(--green-dark); }

  .product {
    position: absolute; text-align: center;
    font-family: "Playfair Display", serif; font-weight: 900; font-size: 30px; line-height: 1.15;
  }
  .label--yellow .product { top: 128px; left: 174px; right: 176px; color: var(--ink); }
  .label--green .product { top: 130px; left: 0; right: 0; color: var(--green); }

  .note { position: absolute; text-align: center; font-size: 10px; }
  .label--yellow .note { top: 206px; left: 174px; right: 176px; color: var(--ink); }
  .label--green .note { top: 206px; left: 0; right: 0; color: var(--green-dark); }

  .volume {
    position: absolute; text-align: center;
    font-family: "Playfair Display", serif; font-weight: 700; font-size: 26px; color: var(--green-dark);
  }
  .label--yellow .volume { top: 276px; left: 174px; right: 176px; }
  .label--green .volume { top: 282px; left: 0; right: 0; }

  .claim {
    position: absolute; right: 24px; top: 24px; text-align: center; transform: rotate(-18deg);
    font-family: "Playfair Display", serif; font-weight: 900; color: var(--green-dark); line-height: 1;
  }
  .claim__big { font-size: 22px; display: block; }
  .claim__small { font-size: 11px; letter-spacing: .5px; display: block; }

  .address { position: absolute; left: 18px; font-size: 8px; line-height: 1.3; color: var(--green); }
  .label--yellow .address { top: 280px; }
  .label--green .address { top: 272px; }
  .registry { position: absolute; left: 18px; font-size: 10px; color: var(--ink); }
  .label--yellow .registry { top: 318px; }
  .label--green .registry { top: 310px; }
</style>
</head>
<body>
<main class="canvas">

  <section class="label label--yellow" aria-label="Etikett Gelb">
    <div class="art art--leaf" role="img" aria-label="Weinblatt-Illustration"></div>
    <div class="art art--vine" role="img" aria-label="Weinblatt hinter dem Mittelfeld"></div>
    <div class="art art--grapes" role="img" aria-label="Weintrauben-Illustration"></div>
    <span class="divider-v divider-v--left"></span>
    <span class="divider-v divider-v--right"></span>
    <p class="brand">Martin Brauer</p>
    <h2 class="product">TRAUBEN<br>SAFT</h2>
    <p class="note">(mit zugesetzter Kohlensäure)</p>
    <p class="volume">0.33l</p>
    <p class="claim"><span class="claim__big">100%</span><span class="claim__small">NATÜRLICH</span></p>
    <p class="address">Weingut Martin Brauer<br>Lindenweg 12<br>79288 Talheim</p>
    <p class="registry">Los Nr. 07/23</p>
  </section>

  <section class="label label--green" aria-label="Etikett Grün">
    <div class="art art--leaf" role="img" aria-label="Helles Weinblatt-Motiv"></div>
    <div class="art art--vine" role="img" aria-label="Helles Weinblatt im Hintergrund"></div>
    <div class="art art--grapes" role="img" aria-label="Helles Weintrauben-Motiv"></div>
    <span class="divider-h divider-h--top"></span>
    <span class="divider-h divider-h--bottom"></span>
    <p class="brand">Martin Brauer</p>
    <h2 class="product">TRAUBEN<br>SAFT</h2>
    <p class="note">(mit zugesetzter Kohlensäure)</p>
    <p class="volume">0.33l</p>
    <p class="claim"><span class="claim__big">100%</span><span class="claim__small">NATÜRLICH</span></p>
    <p class="address">Weingut Martin Brauer<br>Lindenweg 12<br>79288 Talheim</p>
    <p class="registry">Los Nr. 07/23</p>
  </section>

</main>
</body>
</html>
```